Frizzle! A stand up comedy show- poster and other graphics required

We require a design for a new late night comedy show called 'Frizzle!' which will appear at festivals and feature a variety of stand up acts as well as inviting the audience to heckle the comedians on stage. The final design should be bold and stand out loudly, to fit the late night raucous nature of the show.
We need a poster image as well as smaller images for program guides and websites. This is going to be the kind of show people talk about so needs a poster to match!!

Target Market(s)

Comedy fans, 20-40 year olds, late night adult audience

Requirements
Nice to have
• We don't really have any clear design in mind so happy to leave it to interpretation but possible ideas would be: a silhouette of a head shouting / a mic is always an iconic image / the simple outline of an audience with obscenities (@*!& etc) coming out of them / perhaps a mic having fallen over because of a stand-up running off stage!
• But again these are vague ideas. Please message for more info about the show if it helps
Should not have
• Not too busy

```html
<!DOCTYPE html>
<html lang="en">
<head>
<meta charset="utf-8">
<title>Frizzle! – Stand Up Comedy Poster</title>
<link rel="stylesheet" href="https://fonts.googleapis.com/css2?family=Jost:wght@700&family=Arimo:wght@400;700&display=swap">
<style>
  :root {
    --page-bg: #e9e4dc;
    --ink-white: #ffffff;
    --glow-hot: #ffb347;
    --glow-orange: #d9640f;
    --ember: #8a2e06;
    --deep-brown: #3a0f03;
    --night: #140402;
  }
  html, body {
    margin: 0;
    padding: 0;
    width: 914px;
    height: 1200px;
    overflow: hidden;
    background: var(--page-bg);
  }
  .poster {
    position: absolute;
    left: 123px;
    top: 128px;
    width: 668px;
    height: 945px;
    overflow: hidden;
    background: var(--night);
  }
  .poster__photo {
    position: absolute;
    inset: 0;
    background:
      radial-gradient(ellipse 55% 40% at 42% 30%, rgba(255,179,71,0.85), rgba(217,100,15,0.55) 45%, rgba(217,100,15,0) 75%),
      radial-gradient(ellipse 45% 55% at 75% 55%, rgba(230,140,60,0.55), rgba(138,46,6,0) 70%),
      radial-gradient(ellipse 80% 70% at 40% 45%, var(--ember), var(--deep-brown) 65%, var(--night) 100%);
  }
  .poster__title {
    position: absolute;
    left: 0;
    top: 0;
    width: 668px;
    height: 945px;
  }
  .poster__title text {
    font-family: "Jost", "Futura", sans-serif;
    font-weight: 700;
    font-size: 243px;
    fill: var(--ink-white);
  }
  .poster__tagline,
  .poster__blurb {
    position: absolute;
    left: 60px;
    margin: 0;
    color: var(--ink-white);
    font-family: "Arimo", "Arial", sans-serif;
    font-size: 17px;
    line-height: 21.5px;
    text-transform: uppercase;
  }
  .poster__tagline {
    top: 693px;
    font-weight: 700;
  }
  .poster__blurb {
    top: 755px;
    font-weight: 400;
  }
</style>
</head>
<body>
  <main class="poster">
    <div class="poster__photo" role="img" aria-label="Photo of a vintage chrome stage microphone on a stand against warm orange and amber bokeh stage lights"></div>

    <svg class="poster__title" viewBox="0 0 668 945" aria-label="Frizzle!">
      <text transform="translate(229,687) rotate(-90)" x="0" y="0" textLength="685" lengthAdjust="spacingAndGlyphs">FRIZZLE</text>
    </svg>

    <p class="poster__tagline">A variety of<br>stand up acts</p>
    <p class="poster__blurb">Inviting<br>the audience<br>to heckle<br>the comedians<br>on stage</p>
  </main>
</body>
</html>
```